Tiny Brookfells - Haircuts

Flyer - Tiny Brookfells is a independent kids clothes, babywear and toy shop. We sell some of the most beautiful clothes and toys available. We have recently started to do haircuts for kids and we need a flyer to promote this.
The design should be in line with the boutique nature of the shop, the care and attention we pay to each of our customers and lovely items we have for sale. This flyer is primarily to promote the availability of haircuts but will be circulated in the local area to also promote awareness of the shop which only opened a few months ago.

The flyer design should be double sided A5

One side should be all dark blue with just the logo with hair dryer and 'Tiny Brookfells' text with the text below:

Have your child's hair cut at our new salon just for little people! Call 0207 415 2936 or email shop@tinybrookfells-example.com to book an appointment.

Follow us on Chirpline @tinybrookfells

We use the blue background logo and this blue should be the predominant color of the flyer.

Target Market(s)

Discerning parents, mid to high end consumers, high earners..

Industry/Entity Type

Shop

Font styles to use
Other font styles liked:
• Sa

Colors
3177b5
3377b5
85acd3
3076b4

Requirements
Must have
• It would be great to have generic shot of a kid having their haircut. A s hot without copy right issues please.
• Shot of hairdressing, show what the shop looks like.
• Sophisticated feel.
Should not have
• Not a cartoon feel

```html
<!DOCTYPE html>
<html lang="en">
<head>
<meta charset="utf-8">
<title>Tiny Brookfells – Kids Haircuts Flyer</title>
<link rel="stylesheet" href="https://fonts.googleapis.com/css2?family=Gochi+Hand&family=Lato:wght@400&family=Delius&display=swap">
<style>
  :root {
    --page: #e9e6e1;
    --blue: #2a2fc0;
    --blue-deep: #1e22a0;
    --green: #8ccb2c;
    --green-light: #a6db45;
    --white: #ffffff;
    --yellow: #fff200;
    --sky: #33b8f0;
    --lime: #8fe020;
    --red: #ee2a24;
    --brown: #6b4a2a;
    --booking-green: #7cc422;
    --booking-blue: #1e9be6;
    --booking-violet: #4a3fd8;
    --photo-warm: #c9683a;
    --photo-cool: #4a5fa8;
    --photo-shop: #d9cfc8;
  }
  * { margin: 0; padding: 0; box-sizing: border-box; }
  html, body { width: 903px; height: 1200px; overflow: hidden; }
  body { background: var(--page); position: relative; font-family: "Lato", sans-serif; }

  .flyer { position: absolute; overflow: hidden; box-shadow: 0 2px 6px rgba(0,0,0,.2); }
  .flyer-front { left: 72px; top: 40px; width: 740px; height: 525px; background: var(--green); }
  .flyer-back { left: 72px; top: 625px; width: 736px; height: 523px; background: var(--green); }
  .flyer-bg { position: absolute; inset: 0; width: 100%; height: 100%; }

  .photo { position: absolute; border-radius: 50%; border: 6px solid var(--white); }
  .photo-haircut { left: 32px; top: 20px; width: 360px; height: 360px;
    background: radial-gradient(circle at 55% 45%, #e8c9a8 0 22%, var(--photo-warm) 40%, #a8261a 100%);
    box-shadow: 0 0 0 10px var(--green-light); border-color: #f4f07a; }
  .photo-shopfront { left: 408px; top: 178px; width: 250px; height: 250px;
    background: linear-gradient(180deg, var(--photo-cool), #24306a 70%, #7b8aa0); }

  .logo-tab { position: absolute; left: 518px; top: 0; width: 200px; height: 150px; background: var(--white);
    clip-path: polygon(0 0, 100% 0, 100% 82%, 50% 100%, 0 82%);
    display: flex; align-items: center; justify-content: center; gap: 8px; }
  .logo-dot { width: 26px; height: 26px; border-radius: 50%; background: var(--brown); flex: none; }
  .logo-name { font-family: "Gochi Hand", cursive; color: var(--brown); font-size: 32px; line-height: .95; }

  .call-badge { position: absolute; left: 556px; top: 335px; width: 130px; height: 130px; border-radius: 50%;
    background: radial-gradient(circle at 50% 40%, #fff 60%, #ddd); border: 4px solid var(--yellow);
    display: flex; flex-direction: column; align-items: center; justify-content: center; color: var(--red);
    font-family: "Gochi Hand", cursive; }
  .call-badge .call-label { font-size: 30px; line-height: 1; }
  .call-badge .call-number { font-size: 17px; }

  .headline { position: absolute; left: 28px; top: 414px; font-family: "Gochi Hand", cursive; font-size: 42px;
    line-height: 47px; color: var(--white); letter-spacing: 1px; white-space: nowrap; }
  .hl-yellow { color: var(--yellow); }
  .hl-lime { color: var(--lime); }
  .hl-red { color: var(--red); }

  .photo-interior { left: 22px; top: 30px; width: 178px; height: 178px; background: linear-gradient(160deg, #f3eee8, var(--photo-shop) 50%, #9a6b52); box-shadow: 0 0 0 4px var(--yellow); }
  .photo-racks { left: 56px; top: 175px; width: 166px; height: 166px; background: linear-gradient(160deg, #f1e7de, #b73a2e 55%, #3c3a5a); box-shadow: 0 0 0 4px var(--yellow); }
  .photo-umbrella { left: 36px; top: 336px; width: 146px; height: 146px; background: linear-gradient(180deg, #f3efe9, #e0402e 40%, #2f3f8a 80%); box-shadow: 0 0 0 4px var(--yellow); }

  .about-title { position: absolute; left: 222px; top: 55px; width: 476px; height: 46px; background: var(--white);
    font-family: "Delius", cursive; color: var(--red); font-size: 31px; text-align: center; line-height: 46px; }
  .about-text { position: absolute; right: 44px; top: 115px; width: 470px; color: var(--white); font-size: 17.5px;
    line-height: 24px; text-align: right; white-space: nowrap; }
  .launch { position: absolute; right: 44px; top: 225px; text-align: right; font-family: "Gochi Hand", cursive;
    font-size: 44px; line-height: 46px; color: var(--yellow); white-space: nowrap; }
  .launch .sky { color: var(--sky); }
  .launch .red { color: var(--red); }

  .booking { position: absolute; left: 236px; top: 372px; width: 500px; height: 110px; background: var(--white);
    border-left: 10px solid var(--green); border-radius: 10px 0 0 10px; padding: 6px 42px 0 0; text-align: right;
    font-family: "Gochi Hand", cursive; white-space: nowrap; }
  .booking .b-title { color: var(--booking-green); font-size: 27px; line-height: 34px; }
  .booking .b-email { color: var(--booking-blue); font-size: 21px; line-height: 32px; }
  .booking .b-social { color: var(--booking-violet); font-size: 21px; line-height: 32px; }
</style>
</head>
<body>

<section class="flyer flyer-front" aria-label="Flyer front">
  <svg class="flyer-bg" viewBox="0 0 740 525" preserveAspectRatio="none" aria-hidden="true">
    <defs>
      <radialGradient id="frontBlue" cx="60%" cy="70%" r="70%">
        <stop offset="0" stop-color="#3338d6"/><stop offset="1" stop-color="#1c1f9c"/>
      </radialGradient>
    </defs>
    <path d="M0 325 Q 320 440 740 170 L740 525 L0 525 Z" fill="url(#frontBlue)"/>
    <path d="M0 325 Q 320 440 740 170" fill="none" stroke="#ffffff" stroke-width="4"/>
    <path d="M0 512 q 12 -10 24 0 t 24 0 t 24 0 t 24 0 t 24 0 t 24 0 t 24 0 t 24 0 t 24 0 t 24 0 t 24 0 t 24 0 t 24 0 t 24 0 t 24 0 t 24 0 t 24 0 t 24 0 t 24 0 t 24 0 t 24 0 t 24 0 t 24 0 t 24 0 t 24 0 t 24 0 t 24 0 t 24 0 t 24 0 t 24 0 t 24 0 L740 525 L0 525 Z" fill="#ffffff"/>
  </svg>
  <div class="photo photo-haircut" role="img" aria-label="Photo of a toddler having a haircut"></div>
  <div class="photo photo-shopfront" role="img" aria-label="Photo of the shop front"></div>
  <div class="logo-tab"><span class="logo-dot"></span><span class="logo-name">Tiny<br>Brookfells</span></div>
  <div class="call-badge"><span class="call-label">CALL US</span><span class="call-number">0207 415 2936</span></div>
  <p class="headline">Have your child's <span class="hl-yellow">hair cut</span> at<br>our new salon just for <span class="hl-lime">little</span> <span class="hl-red">people</span>!</p>
</section>

<section class="flyer flyer-back" aria-label="Flyer back">
  <svg class="flyer-bg" viewBox="0 0 736 523" preserveAspectRatio="none" aria-hidden="true">
    <defs>
      <radialGradient id="backBlue" cx="60%" cy="50%" r="70%">
        <stop offset="0" stop-color="#3338d6"/><stop offset="1" stop-color="#1c1f9c"/>
      </radialGradient>
    </defs>
    <path d="M0 200 Q 200 60 736 60 L736 523 L0 523 Z" fill="url(#backBlue)"/>
    <path d="M0 200 Q 200 60 736 60" fill="none" stroke="#ffffff" stroke-width="4"/>
    <path d="M0 0 L736 0 L736 14 q -12 10 -24 0 t -24 0 t -24 0 t -24 0 t -24 0 t -24 0 t -24 0 t -24 0 t -24 0 t -24 0 t -24 0 t -24 0 t -24 0 t -24 0 t -24 0 t -24 0 t -24 0 t -24 0 t -24 0 t -24 0 t -24 0 t -24 0 t -24 0 t -24 0 t -24 0 t -24 0 t -24 0 t -24 0 t -24 0 t -24 0 t -24 0 L0 14 Z" fill="#ffffff"/>
    <path d="M0 510 q 12 -10 24 0 t 24 0 t 24 0 t 24 0 t 24 0 t 24 0 t 24 0 t 24 0 t 24 0 t 24 0 t 24 0 t 24 0 t 24 0 t 24 0 t 24 0 t 24 0 t 24 0 t 24 0 t 24 0 t 24 0 t 24 0 t 24 0 t 24 0 t 24 0 t 24 0 t 24 0 t 24 0 t 24 0 t 24 0 t 24 0 t 24 0 L736 523 L0 523 Z" fill="#ffffff"/>
  </svg>
  <div class="photo photo-interior" role="img" aria-label="Photo of the shop interior with clothes shelves"></div>
  <div class="photo photo-racks" role="img" aria-label="Photo of children's clothes on display"></div>
  <div class="photo photo-umbrella" role="img" aria-label="Photo of a kids' umbrella and raincoat"></div>
  <h2 class="about-title">About Tiny Brookfells</h2>
  <p class="about-text">We are a small independent shop selling a fabulous<br>selection of clothes, games and toys for little ones<br>between 0 and 7 years. You will find great brands<br>and everything you'll need for small people.</p>
  <p class="launch">Now we have recently<br><span class="sky">launched</span> to do haircuts<br>for <span class="red">kids</span></p>
  <div class="booking">
    <p class="b-title">For booking an appointment</p>
    <p class="b-email">Email us on shop@tinybrookfells-example.com</p>
    <p class="b-social">Follow us on Chirpline @tinybrookfells</p>
  </div>
</section>

</body>
</html>
```